IT Company seeking creative modern BUSINESS CARD DESIGN!

We are a full service IT company located in California. We specialize in offering computer network support to small to medium to enterprise sized businesses. We are looking for a new business card design to go with our newly designed logo. We prefer business cards that are unique and make a lasting impression. We tend to like business cards with black, gray or blue backgrounds. Our color theme should include black, blue, gray and white only. We want something BOLD, BRIGHT, FUN, CLEAN, and MODERN. Please design with creativity in mind! :) We want our business cards to "pop" and "stand out" when compared to other business cards side by side. We want to be different and make that WINNING first impression every time!! =)

FONT NAME FOR harbor forgeworks is "Cynthe" True Type font.

BLUE LOGO COLOR IS:
Hex: #2375BB
R: 35
G: 117
B: 187

The secondary color is pure "Black". Use of Grayscale is okay too.
Updates

Please look over the sample designs I attached. ** IMPORTANT ** This will give you an idea of the color, design and layouts we like. Also, our logo needs to stand out (nothing small and DO NOT duplicate logo twice on same side of the card. We do want a front and back to the card design. You are welcome to separate the circle logo and the business name if needed. Also, please no pastel colors or busy backgrounds with design. Watermark backgrounds would be okay if it works with the logo design. Let me know if you have any issues opening the logo or font file. Thanks a bunch! EXCITED and AWAITING your designs! I will provide as much feedback as possible. Thank you, Lorna :)

Target Market(s)

Small, Medium to Enterprise businesses. Business Card will be given to professionals. We want the card to stand out and look and feel different.

Industry/Entity Type

Computer

Font styles to use
Sans Serif

Colors
0555a3
ffffff
000000
474747
959595
5c5c5c
c8c8c8
eeeeee
3276b5

Requirements
Must have
• WE WANT TO STAND OUT! BE DIFFERENT! MAKE A LASTING IMPRESSION!

We like clean, neat, modern, BOLD look. See attachment for samples of designs we like.

This is the information needed on the business card. Exact information will change per employee (of course), but heres the required data needed (this info can go on either the front or back of the business card).

Business Logo (File attached)

Gavin Trelawny
CEO / Senior Network Engineer
7190 Dalworth Avenue
Suite F
Modesto, CA 95872

main tel: 209-555-0147
direct tel: 209-555-0182
cell: 209-555-0163
fax tel: 209-xxx-xxxx

gtrelawny@hfgw.example
www.hfgw.example

We really like the use of icons for the address, phone, location etc. Looks modern and clean.

Nice to have
• Somewhere it would be nice to include the cities we are located in and serving:
Modesto - Fresno - Stockton - Pleasanton (FYI - if there's no design space to include these cities, then that's okay. This is just a wish list item to include if theres room. =)

We like watermark background effects if that's an option. Not necessary though.

If there's a way to include we are on Chatterloop, Workmesh, and Chirpline - that would be cool, but not necessary.

Different Card Size or cut ot rounded edges might be cool, but not necessary. We do want to STAND OUT and be different.
Should not have
• No other colors other than Blue, Black, Gray, White. Do not like pastel blue or light blue. For lighter coloring.... would prefer gray scale or white. Keep BLUE color bold and vibrant (like samples I attached).

Do not do a traditional white business card. Too boring and ordinary. Do not make address and phone information in large fat fonts. We want neat and tidy - modern looking fonts. :)

```html
<!DOCTYPE html>
<html lang="en">
<head>
<meta charset="utf-8">
<title>harbor forgeworks — business card</title>
<link rel="stylesheet" href="https://fonts.googleapis.com/css2?family=Montserrat:wght@700&family=Questrial&display=swap">
<style>
  :root {
    --brand-blue: #1a6fba;
    --brand-blue-deep: #0555a3;
    --paper: #ffffff;
    --ink: #000000;
    --stage: #2b2b2b;
    --text-light: #ffffff;
    --text-soft: #e8eef6;
  }
  * { box-sizing: border-box; margin: 0; padding: 0; }
  html, body {
    width: 1200px; height: 1000px; overflow: hidden;
    background: var(--stage);
  }
  .stage {
    position: relative; width: 1200px; height: 1000px;
    display: flex; flex-direction: column; align-items: center; justify-content: center; gap: 60px;
  }
  .card {
    width: 700px; height: 400px; position: relative; overflow: hidden;
    box-shadow: 0 10px 30px rgba(0,0,0,.45);
  }

  /* Front */
  .card--front { display: flex; }
  .front-brand {
    width: 335px; background: var(--paper);
    display: flex; flex-direction: column; align-items: center; justify-content: center; gap: 14px;
  }
  .front-details {
    flex: 1; background: var(--brand-blue); color: var(--text-light);
    font-family: "Questrial", sans-serif; padding: 56px 0 0 40px;
  }

  .brand-mark { width: 62px; height: 62px; border-radius: 50%; background: var(--brand-blue); }
  .card--back .brand-mark { background: var(--paper); width: 66px; height: 66px; }
  .brand-name {
    font-family: "Montserrat", sans-serif; font-weight: 700; font-size: 28px; line-height: 1.05;
    text-align: center; color: var(--brand-blue); letter-spacing: .5px;
  }
  .card--back .brand-name { color: var(--paper); }

  .person-name { font-family: "Montserrat", sans-serif; font-weight: 700; font-size: 24px; }
  .person-title { font-size: 15px; margin-top: 4px; color: var(--text-soft); }
  .address { font-size: 15px; line-height: 1.35; margin-top: 24px; color: var(--text-soft); }
  .phones { list-style: none; margin-top: 22px; font-size: 16px; line-height: 1.55; }
  .phones li { display: flex; align-items: center; gap: 10px; }
  .phones svg { width: 14px; height: 14px; fill: var(--text-light); flex: none; }

  /* Back */
  .card--back {
    background: var(--brand-blue);
    display: flex; flex-direction: column; align-items: center; justify-content: center; gap: 14px;
  }
  .back-contact {
    position: absolute; bottom: 34px; left: 0; right: 0; text-align: center;
    font-family: "Questrial", sans-serif; font-size: 16px; color: var(--text-light);
  }
</style>
</head>
<body>
<main class="stage">
  <section class="card card--back" aria-label="Card back">
    <div class="brand-mark"></div>
    <div class="brand-name">harbor<br>forgeworks</div>
    <p class="back-contact">gtrelawny@hfgw.example &bull; www.hfgw.example</p>
  </section>

  <section class="card card--front" aria-label="Card front">
    <div class="front-brand">
      <div class="brand-mark"></div>
      <div class="brand-name">harbor<br>forgeworks</div>
    </div>
    <div class="front-details">
      <h1 class="person-name">Gavin Trelawny</h1>
      <p class="person-title">CEO / Senior Network Engineer</p>
      <p class="address">7190 Dalworth Avenue<br>Suite F<br>Modesto, CA 95872</p>
      <ul class="phones">
        <li><svg viewBox="0 0 24 24" aria-hidden="true"><path d="M6.6 10.8a15 15 0 0 0 6.6 6.6l2.2-2.2a1 1 0 0 1 1-.25 11.4 11.4 0 0 0 3.6.57 1 1 0 0 1 1 1V20a1 1 0 0 1-1 1A17 17 0 0 1 3 4a1 1 0 0 1 1-1h3.5a1 1 0 0 1 1 1c0 1.25.2 2.45.57 3.57a1 1 0 0 1-.25 1z"/></svg>209-555-0147</li>
        <li><svg viewBox="0 0 24 24" aria-hidden="true"><path d="M6.6 10.8a15 15 0 0 0 6.6 6.6l2.2-2.2a1 1 0 0 1 1-.25 11.4 11.4 0 0 0 3.6.57 1 1 0 0 1 1 1V20a1 1 0 0 1-1 1A17 17 0 0 1 3 4a1 1 0 0 1 1-1h3.5a1 1 0 0 1 1 1c0 1.25.2 2.45.57 3.57a1 1 0 0 1-.25 1z"/></svg>209-555-0182</li>
        <li><svg viewBox="0 0 24 24" aria-hidden="true"><path d="M7 1h10a2 2 0 0 1 2 2v18a2 2 0 0 1-2 2H7a2 2 0 0 1-2-2V3a2 2 0 0 1 2-2zm0 3v14h10V4z"/></svg>209-555-0163</li>
        <li><svg viewBox="0 0 24 24" aria-hidden="true"><path d="M6 2h9l3 3v5H6zM3 11h18a1 1 0 0 1 1 1v8a1 1 0 0 1-1 1H3a1 1 0 0 1-1-1v-8a1 1 0 0 1 1-1zm3 3v2h4v-2z"/></svg>209-xxx-xxxx</li>
      </ul>
    </div>
  </section>
</main>
</body>
</html>
```